Website for Wedding Cake Business based in Suffolk countryside

I need a website to advertise my services. I bake wedding cakes and celebration cakes. My style of baking is very rustic and I use lots of local and homegrown ingredients within my baking. I’d like the website to be classy but countryside chic. I want to website to reflect quality and sophistication but also keep the countryside vibe. My logo is currently a mustard yellow and grey but this may be changed so the colour palette is completely open.

Target Market(s)

Couples and women aged 21-40

Industry/Entity Type

Wedding

Number of Pages Required

4 page

Colors

Designer to choose colors to be used in the design.

Requirements
Must have
• Must appeal to men and women. Must have a contact button, social media links, price list and photo gallery.
• Functioning drop downs (price list, gallery, booking form)
Nice to have
• Very simple layout with menu bar across the top of the page. A section can update which shows which feeding Faye or show I’ll be a next with a map.
Should not have
• Nothing to bold, block coloured or cheesy.

```html
<!DOCTYPE html>
<html lang="en">
<head>
<meta charset="utf-8">
<title>Larkfield Bakehouse – Information</title>
<link href="https://fonts.googleapis.com/css2?family=Karla:wght@400;700&family=Kaushan+Script&family=Raleway:wght@500&display=swap" rel="stylesheet">
<style>
:root{
  --backdrop-dark:#141414;
  --backdrop-mid:#2a2624;
  --page:#ffffff;
  --ink:#1f1f1f;
  --ink-soft:#4a4a4a;
  --nav-blue:#bfd7f1;
  --frame-blue:#b6d1ee;
  --script-blue:#9ec4ea;
  --mint:#aee7c5;
  --link-green:#3fbf5e;
  --footer-green:#a9dbb7;
  --hero-tint:#efe9e6;
  --rule:#222;
}
*{margin:0;padding:0;box-sizing:border-box}
html,body{width:1200px;height:2659px;overflow:hidden}
body{position:relative;font-family:'Karla',sans-serif;color:var(--ink);background:var(--backdrop-dark)}
.backdrop{position:absolute;inset:0;background:radial-gradient(ellipse at 50% 40%,var(--backdrop-mid),var(--backdrop-dark) 70%)}
.page{position:absolute;left:151px;top:67px;width:898px;height:2471px;background:var(--page);border-radius:6px;overflow:hidden}
.hero{position:absolute;left:0;top:0;width:898px;height:580px;background:linear-gradient(160deg,#f3eeeb,var(--hero-tint) 55%,#e8e2de)}
.brand{position:absolute;left:336px;top:39px;width:227px;height:152px;text-align:center}
.brand-name{position:absolute;left:0;right:0;font-weight:700;color:var(--ink);letter-spacing:2px}
.brand .brand-name{top:95px;font-size:36px;line-height:44px}
.tagline{position:absolute;left:0;width:898px;top:201px;text-align:center;font-weight:700;font-size:14px;color:var(--ink)}
.social{position:absolute;display:flex;gap:12px}
.social span{display:block;border-radius:50%;background:#555}
.hero .social{right:52px;top:31px}
.hero .social span{width:48px;height:48px}
.welcome{position:absolute;top:268px;left:0;width:898px;text-align:center;font-family:'Kaushan Script',cursive;font-size:58px;color:#222}
.hero-title{position:absolute;top:346px;left:0;width:898px;text-align:center;font-family:'Raleway',sans-serif;font-weight:500;font-size:52px;letter-spacing:3px;color:#444}
.book-btn{position:absolute;left:289px;top:447px;width:319px;height:58px;background:var(--mint);text-align:center;line-height:58px;font-size:27px;color:#1f1f1f}
.nav{position:absolute;left:0;top:580px;width:898px;height:32px;background:var(--nav-blue);display:flex;justify-content:center}
.nav a{font-size:16px;color:var(--ink);text-decoration:none;line-height:32px;padding:0 23px}
.intro-box{position:absolute;left:47px;top:672px;width:803px;height:229px;border:2px solid var(--frame-blue);text-align:center}
.script-heading{font-family:'Kaushan Script',cursive;font-size:54px;color:var(--script-blue);margin-top:16px;line-height:1.2}
.intro-box p{width:590px;margin:22px auto 0;font-size:18.5px;line-height:22px;color:#333}
.photo{position:absolute}
.photo-tools{left:63px;top:936px;width:332px;height:367px;background:linear-gradient(135deg,#f4f4f4,#e6e1dc 60%,#d9cfc4)}
.about{position:absolute;left:404px;top:938px;width:424px;font-size:13.6px;line-height:18.5px;color:#333;hyphens:auto}
.about p{margin-bottom:18.5px}
.about a{color:var(--link-green);text-decoration:none}
.flavours{position:absolute;left:63px;top:1365px;width:770px;border-collapse:collapse;font-size:13.5px}
.flavours th,.flavours td{border:1.5px solid var(--rule);text-align:left;padding:3px 4px;vertical-align:top;height:30px;line-height:16px}
.flavours th{background:var(--nav-blue);font-weight:700;height:24px}
.flavours .c1{width:160px}.flavours .c2{width:177px}.flavours .c3{width:206px}
.flavours tr.tall td{height:42px}
.pricing{position:absolute;left:63px;top:1685px;width:590px;font-size:15px;line-height:19px;color:#222}
.pricing h2{font-weight:400;font-size:21px;letter-spacing:.5px;line-height:24px;margin-top:22px}
.pricing h2:first-child{margin-top:0}
.price-list{list-style:none;font-size:15.5px;line-height:21px}
.price-list b{font-weight:700}
.pricing p{width:430px}
.photo-cake{left:580px;top:1678px;width:236px;height:478px;background:linear-gradient(180deg,#f7f7f7,#eeeeee 40%,#f2ece6 70%,#f7f7f7)}
.footer-name{position:absolute;left:66px;top:2235px;font-size:42px;color:var(--script-blue);letter-spacing:1px;line-height:44px}
.footer-sub{position:absolute;left:66px;top:2282px;font-size:20px;color:var(--footer-green)}
.footer-address{position:absolute;left:66px;top:2323px;width:230px;font-size:12.5px;line-height:16px;color:#555;font-style:normal}
.footer-contact{position:absolute;left:66px;top:2365px;font-size:12px;line-height:15px;color:var(--script-blue)}
.footer-brand{position:absolute;left:659px;top:2243px;width:175px;height:116px;text-align:center}
.footer-brand .brand-name{top:72px;font-size:29px;line-height:34px}
.footer-tag{position:absolute;left:659px;top:2368px;width:175px;text-align:center;font-weight:700;font-size:11px}
.footer-social{left:715px;top:2399px}
.footer-social span{width:28px;height:28px}
.copyright{position:absolute;left:0;top:2551px;width:1200px;text-align:center;font-size:12px;font-weight:700;color:#e8e8e8}
</style>
</head>
<body>
<div class="backdrop" role="img" aria-label="Dark close-up photograph of a cake as the page background"></div>

<main class="page">
  <header class="hero" role="img" aria-label="Softly faded photograph of iced cupcakes topped with edible flowers on a cooling rack">
    <div class="brand"><span class="brand-name">LARKFIELD</span></div>
    <div class="tagline">Coffee and Bakehouse</div>
    <div class="social" aria-label="Social links"><span aria-label="Social profile one"></span><span aria-label="Social profile two"></span></div>
    <div class="welcome">Welcome to</div>
    <h1 class="hero-title">LARKFIELD BAKEHOUSE</h1>
    <a class="book-btn">Book My Cake</a>
  </header>

  <nav class="nav">
    <a>Home</a><a>Information</a><a>Gallery</a><a>Contact Us</a>
  </nav>

  <section class="intro-box">
    <h2 class="script-heading">Information</h2>
    <p>All of my cakes are hand crafted in my kitchen in Long Melford in Suffolk. Cake is my passion and I create everything from scratch in my 5 starts hygiene rated kitchen.</p>
  </section>

  <div class="photo photo-tools" role="img" aria-label="Baking flat lay with rolling pin, flour, milk, eggs and a sieve on white"></div>

  <section class="about">
    <p>I am lucky enough to have my own allotment where I grow fruit for my homemade jams and preserves as well as edible flowers all grown from seed by me.</p>
    <p>A range of my previous works can be found on the <a>‘Gallery’ page.</a> I work together with you to create the cake of your dreams for your special occasion. I deliver throughout Suffolk, some areas of Cambridgeshire and Essex too.</p>
    <p>Please do visit the <a>‘Contact Us’ page</a> if you would like to hear any further information or have a chat about your requirements.</p>
    <p>If you would like to discuss a quote for a celebration cake other that a Wedding, please do get in touch.</p>
    <p>Please note that for Wedding Cakes, there are some additional charges to the below price list.</p>
    <p>The flavours in the list are also not limited and<br>I always welcome your input!</p>
  </section>

  <table class="flavours">
    <tr><th class="c1">Sponge Flavours</th><th class="c2">Frosting Flavours</th><th class="c3">Other Fillings</th><th>Frosting Types</th></tr>
    <tr><td>Madagascan Vanilla</td><td>Madagascan Vanilla</td><td>Strawberry Conserve</td><td>Italian Meringue Buttercream</td></tr>
    <tr><td>Lemon Bakewell</td><td>Lemon</td><td>Lemon Curd</td><td>Buttercream</td></tr>
    <tr><td>Belgian Chocolate</td><td>Belgian Chocolate</td><td>Cherry Compote</td><td>Cream Cheese</td></tr>
    <tr><td>Carrot Cake</td><td></td><td>Salted Caramel Sauce</td><td></td></tr>
    <tr><td>Lime and Coconut</td><td>Coconut</td><td>Belgian Chocolate Ganache</td><td></td></tr>
    <tr class="tall"><td>White Chocolate and Raspberry</td><td>White Chocolate</td><td>Raspberry Conserve</td><td></td></tr>
    <tr><td></td><td>Salted Caramel</td><td>Lime Marmalade</td><td></td></tr>
  </table>

  <section class="pricing">
    <h2>PRICE GUIDE</h2>
    <ul class="price-list">
      <li><b>One Tier Cake:</b> Serves 40-50 Guests &nbsp;<b>£80</b></li>
      <li><b>Two Tier Cake:</b> Serves 75-85 Guests &nbsp;<b>£160</b></li>
      <li><b>Three Tier Cake:</b> Serves 100-110 Guests &nbsp;<b>£200</b></li>
      <li><b>Large Three Tier Cake:</b> Serves 150-160 &nbsp;<b>£300</b></li>
      <li><b>Four Tier Cake:</b> Serves 115-120 Guests &nbsp;<b>£280</b></li>
      <li><b>Large Four Tier Cake:</b> Serves 190-200 Guests &nbsp;<b>£350</b></li>
    </ul>
    <h2>TASTINGS</h2>
    <p>I offer an option cake tasting prior to booking so you can sample some flavours before making your choice. This is priced at £15 per couple and will be deducted from your final bill if you went ahead with the booking.</p>
    <h2>BOOKING</h2>
    <p>To book your wedding cake we require <b>a deposit of 25% of the total price.</b> Full payment is required 4 weeks before the wedding day.</p>
    <h2>DELIVERY</h2>
    <p>We deliver your wedding cake on the day, and the delivery charges depend on the location and mileage. We contact the venue directly to organise the delivery and set up.</p>
  </section>

  <div class="photo photo-cake" role="img" aria-label="Three-tier white wedding cake with cream roses and a round topper on a white stand"></div>

  <footer>
    <div class="footer-name">Larkfield</div>
    <div class="footer-sub">Bakehouse</div>
    <address class="footer-address">14 Mill Lane, Hartest, Bury Saint Edmunds IP29 4AB, UK</address>
    <div class="footer-contact">e. hello@larkfieldbakehouse.co.uk<br>p. 01632 960418<br>m. 07700 900316</div>
    <div class="footer-brand"><span class="brand-name">LARKFIELD</span></div>
    <div class="footer-tag">Coffee and Bakehouse</div>
    <div class="social footer-social" aria-label="Social links"><span aria-label="Social profile one"></span><span aria-label="Social profile two"></span></div>
  </footer>
</main>

<div class="copyright">Copyright © 2019 Larkfield Bakehouse. &nbsp;All Rights Reserved.</div>
</body>
</html>
```